Cordova Exercise Phone Application Screen Design

We need a sharp professional design for a phone application. We specialize in Health and Fitness Software. This app will be a companion for www.MotionCraftHub.example.
We will be doing all backend and javascript work here and we need someone to create the HTML and CSS for the application which will be developed in Cordova.
For the contest we are submitting three screens. Once we award a winner we will give the winner the first oportunity to bid on the remaining 10 screens.
For the first step of the contest please do the page 1 and page 2 screen design, feel free to submit multiple designs. If we like your designs we will contact you and ask you to design the third page. Once that is done we would like to see the HTML and CSS for the three pages.
Page 1: Simple Home Page
Page 2: Client Search - The search is at the top and the results are below that. The Active | Inactive section is a selection (see https://brivolatech.example/radio-buttons-as-toggle-buttons-with-css/ for an example). Client A has their record expanded (that is what the triangle is). 136 stars should be 136 with Font-Awesome star after the number. To see what the graphs should look like please see the attached png. Then a list is below the stars and graphs.
Page 3/4: Step 1 of 3 - When the magnifying glass is selected a flyout with the search criteria comes out (page 3). Criteria is selected and the results are shown (page 4).
The default width should be 320 but the application should look good on all phones and tablets.
Please feel free to contact us with questions. The winner will get more work of a similar nature.

Target Market(s)
Physical Therapists
Font styles to use
Colors
Designer to choose colors to be used in the design.
Requirements
Must have
- Clean and easy to understand design. Look professional and uncluttered. Be easy to understand and use. Must have the logo at the top (just the MCH logo is fine)
Should not have
- Cartoonish look and feel.

```html
<!DOCTYPE html>
<html lang="en">
<head>
<meta charset="utf-8">
<title>MCH – Client Search</title>
<link rel="stylesheet" href="https://fonts.googleapis.com/css2?family=Roboto:wght@400;500;700;900&display=swap">
<style>
:root{
  --stage:#c4c4c4;
  --screen:#ffffff;
  --page:#f1f1f1;
  --field:#f3f3f3;
  --ink:#111111;
  --text:#555555;
  --muted:#9a9a9a;
  --blue:#2196f3;
  --teal-a:#2fd3a6;
  --teal-b:#17bed8;
  --alert:#f23b2e;
  --weight:#f4511e;
  --line:#e4e4e4;
  --subhead:#e6e6e6;
}
*{box-sizing:border-box;margin:0;padding:0}
html,body{width:1200px;height:1200px;overflow:hidden}
body{background:var(--stage);font-family:'Roboto',sans-serif;position:relative}
.app-screen{
  position:absolute;left:327px;top:10px;width:578px;height:1250px;
  transform:scale(.944);transform-origin:top left;
  background:var(--page);border-radius:44px;overflow:hidden;
}
.abs{position:absolute}
.status-bar{left:0;top:0;width:578px;height:70px;background:var(--screen)}
.status-time{left:48px;top:20px;font-size:22px;font-weight:500;color:var(--ink)}
.status-icons{right:22px;top:24px}
.app-header{left:0;top:70px;width:578px;height:110px;background:var(--screen);border-bottom:1px solid var(--line)}
.brand{left:33px;top:46px;font-size:30px;font-weight:900;letter-spacing:4px;color:var(--ink)}
.screen-title{left:0;width:578px;top:50px;text-align:center;font-size:27px;font-weight:500;color:var(--ink)}
.inbox{left:445px;top:52px}
.badge{left:465px;top:45px;width:20px;height:20px;border-radius:50%;background:var(--alert);color:#fff;font-size:13px;font-weight:700;text-align:center;line-height:20px}
.help{left:513px;top:51px;width:32px;height:32px;border-radius:50%;background:var(--blue);color:#fff;font-size:22px;font-weight:700;text-align:center;line-height:32px}

.search-card{left:16px;top:202px;width:546px;height:508px;background:var(--screen)}
.field{left:17px;width:513px;height:60px;background:var(--field)}
.field svg{position:absolute;left:24px;top:16px}
.field-label{position:absolute;left:77px;top:17px;font-size:22px;color:var(--muted)}
.field .calendar{left:auto;right:20px;top:15px}
.status-toggle{left:17px;top:317px;width:513px;height:60px;background:var(--field);display:flex}
.status-toggle span{flex:1;display:flex;align-items:center;justify-content:center;font-size:22px;font-weight:500;color:var(--muted)}
.status-toggle .is-on{background:var(--blue);color:#fff;flex:0 0 256px}
.search-button{left:17px;top:415px;width:513px;height:60px;background:linear-gradient(90deg,var(--teal-a),var(--teal-b));color:#fff;font-size:22px;font-weight:500;display:flex;align-items:center;justify-content:center}

.results{left:16px;top:727px;width:546px;height:520px;background:var(--screen)}
.results-head{left:0;top:0;width:546px;height:61px;background:var(--ink);color:#fff;font-size:20px;font-weight:700}
.results-head span,.client-row span,.client-row svg{position:absolute;top:50%;transform:translateY(-50%)}
.c1{left:17px}.c2{left:184px}.c3{left:313px}
.client-row{left:0;width:546px;height:80px;border-bottom:1px solid var(--line);font-size:20px;color:var(--text)}
.client-row .weights{left:436px}
.client-row .chev{left:509px}
.detail{left:0;top:141px;width:546px;height:181px;border-bottom:1px solid var(--line);color:var(--text)}
.detail-meta{top:17px;font-size:17px}
.plan-head{left:17px;top:51px;width:513px;height:38px;background:var(--subhead);font-size:15px;font-weight:500;color:#333}
.plan-head span,.plan-row span{position:absolute;top:50%;transform:translateY(-50%)}
.p1{left:19px}.p2{left:163px}
.plan-row{left:17px;width:513px;height:30px;font-size:15px;color:#444}
.action-select{left:297px;width:194px;height:26px;background:var(--field);border-radius:2px}
.action-select span{left:15px}
.action-select svg{position:absolute;right:10px;top:9px}

.tab-bar{left:0;top:1164px;width:578px;height:86px;background:var(--screen);border-top:1px solid var(--line)}
.tab{top:0;width:120px;height:86px;margin-left:-60px;text-align:center;color:var(--muted);font-size:18px}
.tab svg{display:block;margin:12px auto 4px}
.tab.is-current{color:var(--ink)}
</style>
</head>
<body>
<main class="app-screen">
  <div class="abs status-bar">
    <span class="abs status-time">9:41</span>
    <svg class="abs status-icons" width="104" height="20" viewBox="0 0 104 20">
      <rect x="0" y="12" width="4" height="6" fill="#111"/><rect x="6" y="9" width="4" height="9" fill="#111"/><rect x="12" y="5" width="4" height="13" fill="#111"/><rect x="18" y="1" width="4" height="17" fill="#111"/>
      <path d="M34 7a14 14 0 0 1 20 0M37 10.5a9 9 0 0 1 14 0M40.5 14a4 4 0 0 1 7 0" stroke="#111" stroke-width="2.5" fill="none"/>
      <rect x="66" y="2" width="33" height="15" rx="3" stroke="#111" stroke-width="1.6" fill="none"/><rect x="68.5" y="4.5" width="28" height="10" rx="1.5" fill="#111"/><rect x="100.5" y="7" width="2" height="5" fill="#111"/>
    </svg>
  </div>

  <header class="abs app-header">
    <span class="abs brand">MCH</span>
    <h1 class="abs screen-title">CLIENT SEARCH</h1>
    <svg class="abs inbox" width="34" height="24" viewBox="0 0 34 24"><rect x="1" y="1" width="32" height="22" rx="2" fill="#d8dde2"/><path d="M1 2l16 12L33 2" stroke="#b6bdc4" stroke-width="2" fill="none"/></svg>
    <span class="abs badge">2</span>
    <span class="abs help">?</span>
  </header>

  <section class="abs search-card">
    <div class="abs field" style="top:28px">
      <svg width="28" height="28" viewBox="0 0 28 28" fill="none" stroke="#555" stroke-width="2"><circle cx="14" cy="9" r="6"/><path d="M3 27c1-7 6-10 11-10s10 3 11 10"/></svg>
      <span class="field-label">First Name</span>
    </div>
    <div class="abs field" style="top:100px">
      <svg width="28" height="28" viewBox="0 0 28 28" fill="none" stroke="#555" stroke-width="2"><circle cx="14" cy="9" r="6"/><path d="M3 27c1-7 6-10 11-10s10 3 11 10"/></svg>
      <span class="field-label">Last Name</span>
    </div>
    <div class="abs field" style="top:173px">
      <svg width="36" height="28" viewBox="0 0 36 28" fill="none" stroke="#555" stroke-width="2"><rect x="1" y="3" width="34" height="22" rx="2"/><circle cx="11" cy="12" r="3"/><path d="M5 20c1-4 11-4 12 0M21 10h10M21 14h10M21 18h10"/></svg>
      <span class="field-label">Client Id</span>
    </div>
    <div class="abs field" style="top:245px">
      <svg width="34" height="32" viewBox="0 0 34 32" fill="none" stroke="#555" stroke-width="2"><rect x="5" y="8" width="27" height="22" rx="2"/><circle cx="10" cy="10" r="8" fill="#f3f3f3"/><path d="M10 6v5h3M16 20h3M22 20h3M16 25h3M22 25h3"/></svg>
      <span class="field-label">DOB</span>
      <svg class="abs calendar" width="32" height="32" viewBox="0 0 32 32"><rect x="1" y="4" width="30" height="27" rx="3" fill="#e2e6ea"/><rect x="1" y="4" width="30" height="8" rx="3" fill="#f0463c"/><rect x="8" y="1" width="3" height="7" fill="#c0392b"/><rect x="21" y="1" width="3" height="7" fill="#c0392b"/><g fill="#9aa3ad"><rect x="6" y="15" width="4" height="3"/><rect x="12" y="15" width="4" height="3"/><rect x="18" y="15" width="4" height="3"/><rect x="24" y="15" width="3" height="3"/><rect x="6" y="20" width="4" height="3"/><rect x="12" y="20" width="4" height="3"/><rect x="18" y="20" width="4" height="3"/><rect x="24" y="20" width="3" height="3"/><rect x="6" y="25" width="4" height="3"/><rect x="12" y="25" width="4" height="3"/><rect x="18" y="25" width="4" height="3"/></g></svg>
    </div>
    <div class="abs status-toggle"><span class="is-on">Active</span><span>Inactive</span></div>
    <div class="abs search-button">Search</div>
  </section>

  <section class="abs results">
    <div class="abs results-head"><span class="c1">Client Name</span><span class="c2">Client Id</span><span class="c3">DOB</span></div>

    <div class="abs client-row" style="top:61px">
      <span class="c1">Client A</span><span class="c2">123ABC</span><span class="c3">1/1/1979</span>
      <svg class="weights" width="36" height="24" viewBox="0 0 36 24" fill="var(--weight)"><rect x="0" y="10" width="36" height="4"/><rect x="4" y="4" width="5" height="16" rx="1"/><rect x="10" y="1" width="4" height="22" rx="1"/><rect x="27" y="4" width="5" height="16" rx="1"/><rect x="22" y="1" width="4" height="22" rx="1"/></svg>
      <svg class="chev" width="18" height="12" viewBox="0 0 18 12" fill="none" stroke="#111" stroke-width="2.2"><path d="M2 10l7-7 7 7"/></svg>
    </div>

    <div class="abs detail">
      <span class="abs detail-meta c1">136 Stars</span>
      <span class="abs detail-meta c2">Pain/Difficulty Graph</span>
      <div class="abs plan-head"><span class="p1">Issued</span><span class="p2">Expiration</span></div>
      <div class="abs plan-row" style="top:94px"><span class="p1">1/1/2019</span><span class="p2">1/1/2019</span>
        <div class="abs action-select" style="top:2px"><span>Action</span><svg width="11" height="7" viewBox="0 0 11 7" fill="none" stroke="#555" stroke-width="1.5"><path d="M1 1l4.5 4.5L10 1"/></svg></div>
      </div>
      <div class="abs plan-row" style="top:130px"><span class="p1">1/1/2019</span><span class="p2">1/1/2019</span>
        <div class="abs action-select" style="top:2px"><span>Action</span><svg width="11" height="7" viewBox="0 0 11 7" fill="none" stroke="#555" stroke-width="1.5"><path d="M1 1l4.5 4.5L10 1"/></svg></div>
      </div>
    </div>

    <div class="abs client-row" style="top:322px">
      <span class="c1">Client B</span><span class="c2">123ABC</span><span class="c3">1/1/1979</span>
      <svg class="weights" width="36" height="24" viewBox="0 0 36 24" fill="var(--weight)"><rect x="0" y="10" width="36" height="4"/><rect x="4" y="4" width="5" height="16" rx="1"/><rect x="10" y="1" width="4" height="22" rx="1"/><rect x="27" y="4" width="5" height="16" rx="1"/><rect x="22" y="1" width="4" height="22" rx="1"/></svg>
      <svg class="chev" width="18" height="12" viewBox="0 0 18 12" fill="none" stroke="#111" stroke-width="2.2"><path d="M2 2l7 7 7-7"/></svg>
    </div>

    <div class="abs client-row" style="top:402px">
      <span class="c1">Client C</span><span class="c2">123ABC</span><span class="c3">1/1/1979</span>
      <svg class="weights" width="36" height="24" viewBox="0 0 36 24" fill="var(--weight)"><rect x="0" y="10" width="36" height="4"/><rect x="4" y="4" width="5" height="16" rx="1"/><rect x="10" y="1" width="4" height="22" rx="1"/><rect x="27" y="4" width="5" height="16" rx="1"/><rect x="22" y="1" width="4" height="22" rx="1"/></svg>
      <svg class="chev" width="18" height="12" viewBox="0 0 18 12" fill="none" stroke="#111" stroke-width="2.2"><path d="M2 2l7 7 7-7"/></svg>
    </div>
  </section>

  <nav class="abs tab-bar">
    <div class="abs tab" style="left:72px">
      <svg width="34" height="32" viewBox="0 0 34 32" fill="none" stroke="#8a8a8a" stroke-width="2"><path d="M2 2h30v20H14l-7 7v-7H2z"/><circle cx="11" cy="12" r="1.5" fill="#8a8a8a"/><circle cx="17" cy="12" r="1.5" fill="#8a8a8a"/><circle cx="23" cy="12" r="1.5" fill="#8a8a8a"/></svg>Messages
    </div>
    <div class="abs tab is-current" style="left:181px">
      <svg width="34" height="32" viewBox="0 0 34 32" fill="none" stroke="#111" stroke-width="2.4"><circle cx="14" cy="13" r="11"/><path d="M22 21l10 10"/></svg>Search
    </div>
    <div class="abs tab" style="left:289px">
      <svg width="40" height="32" viewBox="0 0 40 32" fill="none" stroke="#8a8a8a" stroke-width="2"><circle cx="20" cy="9" r="6"/><circle cx="9" cy="12" r="4"/><circle cx="31" cy="12" r="4"/><path d="M9 30c0-8 5-13 11-13s11 5 11 13M1 27c0-5 3-8 7-8M39 27c0-5-3-8-7-8"/></svg>Add Client
    </div>
    <div class="abs tab" style="left:398px">
      <svg width="30" height="32" viewBox="0 0 30 32" fill="none" stroke="#8a8a8a" stroke-width="2"><rect x="3" y="2" width="24" height="28" rx="1"/><path d="M15 7v18M10 12l5-5 5 5M10 20l5 5 5-5"/></svg>Protocols
    </div>
    <div class="abs tab" style="left:506px">
      <svg width="34" height="32" viewBox="0 0 34 34" fill="none" stroke="#8a8a8a" stroke-width="2"><circle cx="17" cy="17" r="5"/><path d="M14 2h6l1 4 4 2 4-2 4 5-3 3v4l3 3-4 5-4-2-4 2-1 4h-6l-1-4-4-2-4 2-4-5 3-3v-4L1 11l4-5 4 2 4-2z"/></svg>Settings
    </div>
  </nav>
</main>
</body>
</html>
```